Little ShopTalk w/Merin Voss (podcast)

Podcast graphic to attract listeners interested in small business tax, bookkeeping and payroll issues. Little ShopTalk w/Merin Voss. Simple, clever and clear. Bold colors that attract attention and make small business owners interested in listening to her and wanting to get to know her. We want to her to appear to be a coach and expert on small business.

Target Market(s)

women and men in small business

Industry/Entity Type

Business Consultant

Font styles to use
Sans Serif

Colors
b260a6
f78f20
32a6d7

Requirements
Must have
• Warm and inviting, positive and uplifting. Promote a personable lady ready and willing to loyally serve her clients and help them succeed in business.
Nice to have
• Clever and smart attracting people that want her business service and advice.
• Emphasize her warmness and open personality.
Should not have
• Nasty or inappropriate,

```html
<!DOCTYPE html>
<html lang="en">
<head>
<meta charset="utf-8">
<title>Little ShopTalk w/Merin Voss</title>
<link rel="stylesheet" href="https://fonts.googleapis.com/css2?family=Fredoka:wght@700&display=swap">
<style>
  :root {
    --blue: #32a6d7;
    --purple: #b260a6;
    --orange: #f78f20;
    --white: #ffffff;
    --navy: #0f4a6e;
    --bubble: #cff6f8;
    --wall-pink: #ecc6dc;
    --wall-teal: #7fd3d6;
    --wall-orange: #f39a3a;
    --wall-magenta: #d65aa3;
    --hair: #2a1a1c;
    --skin: #e9b49a;
    --top-orange: #e68a22;
  }
  * { margin: 0; padding: 0; box-sizing: border-box; }
  html, body { width: 1200px; height: 794px; overflow: hidden; background: var(--white); }
  .episode-card {
    position: relative;
    width: 1200px;
    height: 794px;
    overflow: hidden;
    font-family: "Fredoka", "Arial Rounded MT Bold", sans-serif;
  }
  .mural-backdrop {
    position: absolute;
    inset: 0;
    background:
      radial-gradient(ellipse 160px 260px at 120px 560px, var(--wall-teal) 0%, rgba(127,211,214,0) 100%),
      radial-gradient(ellipse 110px 140px at 120px 90px, var(--wall-teal) 0%, rgba(127,211,214,0) 100%),
      radial-gradient(ellipse 200px 360px at 520px 320px, var(--wall-orange) 0%, rgba(243,154,58,0) 100%),
      radial-gradient(ellipse 200px 300px at 1130px 300px, var(--wall-magenta) 0%, rgba(214,90,163,0) 100%),
      radial-gradient(ellipse 160px 200px at 520px 700px, var(--wall-magenta) 0%, rgba(214,90,163,0) 100%),
      linear-gradient(100deg, var(--wall-pink) 0%, #e9b9cf 40%, #f0a860 55%, #ecc3d8 100%);
  }
  .host-photo {
    position: absolute;
    left: 610px;
    top: 36px;
    width: 560px;
    height: 758px;
    border-radius: 260px 260px 0 0;
    background:
      radial-gradient(ellipse 170px 220px at 300px 260px, var(--skin) 0%, rgba(233,180,154,0.9) 60%, rgba(233,180,154,0) 100%),
      linear-gradient(180deg, var(--hair) 0%, var(--hair) 45%, var(--top-orange) 58%, var(--top-orange) 100%);
  }
  .show-title {
    position: absolute;
    font-weight: 700;
    line-height: 1;
    white-space: nowrap;
    paint-order: stroke fill;
    -webkit-text-stroke: 8px var(--white);
    transform-origin: left center;
  }
  .show-name {
    left: 36px;
    top: 88px;
    font-size: 84px;
    color: var(--blue);
    transform: rotate(-3deg);
    letter-spacing: 1px;
  }
  .show-with {
    left: 248px;
    top: 246px;
    font-size: 64px;
    color: var(--purple);
    -webkit-text-stroke: 6px var(--white);
  }
  .host-name {
    left: 64px;
    top: 346px;
    font-size: 112px;
    color: var(--orange);
    letter-spacing: 2px;
  }
  .network-mark {
    position: absolute;
    left: 168px;
    top: 580px;
    display: flex;
    align-items: center;
    gap: 14px;
    font-weight: 700;
    font-size: 30px;
    line-height: 1.05;
    color: var(--navy);
  }
  .network-dot {
    width: 64px;
    height: 64px;
    border-radius: 50%;
    background: var(--bubble);
    flex: none;
  }
</style>
</head>
<body>
  <main class="episode-card">
    <div class="mural-backdrop" role="img" aria-label="Blurred colourful painted mural wall in pink, teal, orange and magenta"></div>
    <div class="host-photo" role="img" aria-label="Photo of host Merin Voss with long dark hair and an orange top, smiling over her shoulder"></div>
    <h1 class="show-title show-name">Little ShopTalk</h1>
    <p class="show-title show-with">With</p>
    <p class="show-title host-name">Merin Voss</p>
    <div class="network-mark">
      <span class="network-dot"></span>
      <span class="network-name">Brightwit<br>Women Podcast</span>
    </div>
  </main>
</body>
</html>
```